Zumbly - New Payment App for Student

Zum-bly - A Payment App for student to make payment, track own expenses and practice good dietary habits. The App theme is Fun and excitement.
Target User: Secondary Student aged 13-18
Look and Feel: Fun, excitement and simple.
Screen 1
Login to the app using thumbprints or password
Screen 2
Display the balance
Wallet balance >>> go to screen 3 to display transaction history
Gamification balance - points + badges >>> go to screen 3
Button to make payment
Screen 2-1
Allow them to do payment
Click “Pay”
Display QR code
scanning by merchant
Payment made
Notification received
The transaction history will be shown up
Screen 2-2
Allow them to top up (alternatively to parent Top-up using credit card)
Click “Top Up”
Display QR code
Pass the cash to merchant
scanning by merchant
Payment made
Notification received
The new balance will be shown up
Screen 3
Display more details on transaction history
Payment history + gamification history (gain/redeem points)
E.g. 14 Nov Canteen purchase $5.40
- Banana +30 points
- Milk +10 points
Screen 4 (play a game to earn point)
Introduce some trivial games (while waiting in line at cafeteria or school store) to gain some points
Crosswords
Puzzle
Screen 5 (Display achievements)
Leaderboard
Where the individual stands in the class
Where the class stands overall in school
Badges
Level
Achievements
For more, please go to our website http://www.zumbly-pay.example/
Target Market(s)
Secondary School Student aged 13-18
Industry/Entity Type
Education
Logo Text
zumbly
Look and feel

```html
<!DOCTYPE html>
<html lang="en">
<head>
<meta charset="utf-8">
<title>Zumbly – Student Payment App Screens</title>
<link rel="stylesheet" href="https://fonts.googleapis.com/css2?family=Jura:wght@400;600&display=swap">
<style>
  :root {
    --stage-top: #3f69a3;
    --stage-bottom: #8f8479;
    --screen-bg: #17191b;
    --neon: #5ef2f5;
    --neon-soft: rgba(94, 242, 245, 0.55);
    --neon-glow: rgba(94, 242, 245, 0.35);
    --tab-light: #e9fbfc;
    --tab-mid: #aeeff1;
    --text-light: #e6f4f5;
    --pay-orange: #f7a35c;
    --pay-orange-light: #ffd2a4;
    --pay-text: #5a3416;
    --bar-yellow: #f2e23a;
    --bar-magenta: #e64fd9;
  }

  * { box-sizing: border-box; margin: 0; padding: 0; }

  html, body {
    width: 902px;
    height: 1200px;
    overflow: hidden;
  }

  body {
    background: linear-gradient(160deg, var(--stage-top), var(--stage-bottom));
    font-family: "Jura", sans-serif;
    color: var(--text-light);
    position: relative;
  }

  .screen {
    position: absolute;
    top: 210px;
    width: 400px;
    height: 780px;
    background: var(--screen-bg);
    border-radius: 6px;
    overflow: hidden;
  }
  .screen--login { left: 34px; }
  .screen--wallet { left: 468px; }

  .brand {
    position: absolute;
    top: 28px;
    left: 0;
    right: 0;
    text-align: center;
    font-size: 42px;
    font-weight: 600;
    letter-spacing: 2px;
    color: var(--neon);
    text-transform: uppercase;
  }

  /* Login screen */
  .fingerprint {
    position: absolute;
    top: 190px;
    left: 150px;
    width: 100px;
    height: 140px;
    border-radius: 48px;
    background: radial-gradient(circle, #1f7f86, #123b40 75%);
  }

  .pill-button {
    position: absolute;
    height: 30px;
    padding: 0 16px;
    border-radius: 15px;
    background: linear-gradient(#ffffff, #bfeff1);
    box-shadow: 0 0 10px var(--neon-glow);
    color: #2c5f63;
    font-size: 14px;
    line-height: 30px;
    letter-spacing: 1px;
    text-transform: uppercase;
  }
  .pill-button--scan { top: 360px; right: 36px; }
  .pill-button--login { top: 650px; right: 36px; }

  .divider {
    position: absolute;
    top: 430px;
    left: 36px;
    right: 36px;
    height: 2px;
    background: var(--neon);
    box-shadow: 0 0 6px var(--neon-glow);
  }

  .field {
    position: absolute;
    left: 40px;
    right: 36px;
    height: 46px;
    border: 2px solid var(--neon);
    border-radius: 23px;
    box-shadow: 0 0 10px var(--neon-glow), inset 0 0 6px var(--neon-glow);
    padding: 0 18px;
    font-size: 17px;
    line-height: 42px;
    letter-spacing: 1px;
    color: var(--neon-soft);
  }
  .field--user { top: 510px; }
  .field--password { top: 580px; color: var(--text-light); letter-spacing: 4px; font-size: 22px; }

  .register-link {
    position: absolute;
    top: 670px;
    left: 40px;
    font-size: 12px;
    letter-spacing: 1px;
    color: var(--neon);
    text-transform: uppercase;
  }

  /* Wallet screen */
  .icon { position: absolute; }
  .icon--back { top: 36px; left: 18px; }
  .icon--menu { top: 70px; right: 14px; }

  .wallet-section {
    position: absolute;
    left: 22px;
    right: 22px;
    height: 120px;
  }
  .wallet-section--balance { top: 110px; }
  .wallet-section--history { top: 250px; }
  .wallet-section--points { top: 390px; }
  .wallet-section--badges { top: 530px; }

  .section-tab {
    position: absolute;
    top: 0;
    left: 30px;
    right: 14px;
    height: 58px;
    border-radius: 22px 22px 4px 4px;
    background: linear-gradient(var(--tab-light), var(--tab-mid));
    box-shadow: 0 0 14px var(--neon-glow);
    text-align: center;
    font-size: 22px;
    line-height: 58px;
    letter-spacing: 1px;
    color: var(--neon);
  }
  .section-tab--caps { text-transform: uppercase; }

  .section-row {
    position: absolute;
    top: 62px;
    left: 0;
    right: 0;
    height: 48px;
    border: 2px solid var(--neon);
    border-radius: 24px;
    box-shadow: 0 0 10px var(--neon-glow);
    padding: 0 16px;
    font-size: 16px;
    letter-spacing: 1px;
    display: flex;
    justify-content: space-between;
    align-items: center;
  }

  .balance-amount { color: var(--neon); font-size: 19px; }

  .view-all {
    height: 26px;
    padding: 0 12px;
    border-radius: 13px;
    background: linear-gradient(#ffffff, #bfeff1);
    color: #2c5f63;
    font-size: 11px;
    line-height: 26px;
  }

  .make-payment {
    position: absolute;
    top: 690px;
    left: 110px;
    width: 180px;
    height: 36px;
    border-radius: 10px;
    background: linear-gradient(var(--pay-orange-light), var(--pay-orange));
    box-shadow: 0 0 10px rgba(247, 163, 92, 0.5);
    color: var(--pay-text);
    text-align: center;
    font-size: 16px;
    line-height: 36px;
    letter-spacing: 1px;
  }

  .status-bar {
    position: absolute;
    top: 744px;
    left: 18px;
    right: 12px;
    display: flex;
    align-items: center;
    gap: 34px;
    font-size: 16px;
  }
  .status-item { display: flex; align-items: center; gap: 8px; }
  .status-item--level { margin-left: auto; font-size: 8px; gap: 4px; flex-direction: column; align-items: flex-start; }
  .bars { display: flex; gap: 2px; height: 14px; }
  .bars span { width: 2px; height: 100%; }
  .bars--yellow span { background: var(--bar-yellow); }
  .bars--magenta span { background: var(--bar-magenta); }
  .bars--cyan span { background: var(--neon); }
</style>
</head>
<body>

  <section class="screen screen--login" aria-label="Login screen">
    <div class="brand">Zumbly</div>
    <div class="fingerprint" role="img" aria-label="Glowing fingerprint scan illustration"></div>
    <div class="pill-button pill-button--scan">Scan</div>
    <div class="divider"></div>
    <div class="field field--user">user name</div>
    <div class="field field--password">•••••</div>
    <div class="register-link">Register</div>
    <div class="pill-button pill-button--login">Login</div>
  </section>

  <section class="screen screen--wallet" aria-label="Wallet screen">
    <svg class="icon icon--back" width="34" height="26" viewBox="0 0 34 26" aria-label="Back">
      <path d="M32 13H4M14 3L3 13l11 10" fill="none" stroke="var(--neon)" stroke-width="3.5" stroke-linecap="round" stroke-linejoin="round"/>
    </svg>
    <div class="brand">Zumbly</div>
    <svg class="icon icon--menu" width="22" height="20" viewBox="0 0 22 20" aria-label="Menu">
      <path d="M1 3h20M1 10h20M1 17h20" stroke="var(--neon)" stroke-width="3"/>
    </svg>

    <div class="wallet-section wallet-section--balance">
      <div class="section-tab section-tab--caps">Wallet Balance</div>
      <div class="section-row"><span>Available Balance</span><span class="balance-amount">S$ 92.36</span></div>
    </div>
    <div class="wallet-section wallet-section--history">
      <div class="section-tab">Transaction History</div>
      <div class="section-row"><span>Transaction History</span><span class="view-all">view all</span></div>
    </div>
    <div class="wallet-section wallet-section--points">
      <div class="section-tab">Points</div>
      <div class="section-row"><span>Available game points</span><span class="view-all">view all</span></div>
    </div>
    <div class="wallet-section wallet-section--badges">
      <div class="section-tab">Badges</div>
      <div class="section-row"><span>Earn Badges</span><span class="view-all">view all</span></div>
    </div>

    <div class="make-payment">Make Payment</div>

    <div class="status-bar">
      <div class="status-item">
        <div class="bars bars--yellow"><span></span><span></span><span></span></div>03
      </div>
      <div class="status-item">
        <div class="bars bars--magenta"><span></span><span></span><span></span><span></span><span></span><span></span><span></span><span></span><span></span><span></span></div>10
      </div>
      <div class="status-item status-item--level">
        <div class="bars bars--cyan"><span></span><span></span><span></span><span></span></div>
        Level 02 16x done
      </div>
    </div>
  </section>

</body>
</html>
```